New Business Card Design Project

Looking for a modern business card design for an import distribution business for industrial technical products. The winning design will translate modern, sophistication, technical, professional and sustainable.

Target Market(s)

Technical customers

Industry/Entity Type

Business

Contact Information for Business Card

Dean Harlow
Sales Manager
M: 0471 625 183
P: 1300 872 619
dean@volkarsystems.com.au
4/18 Galloway Crest Road
Marlow Heights NSW 2184
www.volkarsystems.com.au

Font styles to use
Sans Serif

Colors
ec1f27
606060
000000
fbfbfb

Requirements
Must have
• My Logo which is the Volkar Systems logo attached
Nice to have
• Eurostile Bold font

```html
<!DOCTYPE html>
<html lang="en">
<head>
<meta charset="utf-8">
<title>Volkar Systems – Business Card</title>
<link rel="stylesheet" href="https://fonts.googleapis.com/css2?family=Roboto:wght@400;700&display=swap">
<style>
  :root {
    --red: #ec1f27;
    --grey: #606060;
    --slate: #6b7078;
    --back-grey: #878c93;
    --black: #000000;
    --paper: #fbfbfb;
    --stage: #e4e5e7;
    --rule: #b7b9bc;
  }
  * { box-sizing: border-box; margin: 0; padding: 0; }
  html, body { width: 1200px; height: 800px; overflow: hidden; }
  body {
    background: var(--stage);
    font-family: "Roboto", Arial, sans-serif;
    position: relative;
  }
  .card {
    position: absolute;
    top: 245px;
    width: 540px;
    height: 310px;
    overflow: hidden;
    box-shadow: 0 6px 18px rgba(0,0,0,0.15);
  }

  /* Back side */
  .card-back { left: 30px; background: var(--back-grey); }
  .card-back .brand {
    position: absolute; inset: 0;
    display: flex; align-items: center; justify-content: center; gap: 14px;
  }
  .card-back .brand-mark { width: 34px; height: 34px; background: var(--paper); }
  .card-back .brand-name {
    color: var(--paper); font-weight: 700; font-size: 40px; letter-spacing: 2px;
  }

  /* Front side */
  .card-front { left: 630px; background: var(--paper); }
  .band { position: absolute; }
  .band-top-grey { top: 0; left: 0; width: 100%; height: 14px; background: var(--slate); }
  .band-top-red { top: 14px; right: 0; width: 190px; height: 22px; background: var(--red); }
  .band-bottom-red { bottom: 14px; left: 0; width: 170px; height: 14px; background: var(--red); }
  .band-bottom-grey { bottom: 0; left: 0; width: 100%; height: 14px; background: var(--slate); }

  .card-front .brand {
    position: absolute; top: 66px; left: 150px;
    display: flex; align-items: center; gap: 12px;
  }
  .card-front .brand-mark { width: 30px; height: 30px; background: var(--red); }
  .card-front .brand-name {
    color: var(--red); font-weight: 700; font-size: 34px; letter-spacing: 1.5px;
  }

  .person { position: absolute; top: 148px; left: 36px; }
  .person-name { font-size: 19px; font-weight: 400; letter-spacing: 0.5px; color: var(--grey); }
  .person-name .first { color: var(--red); }
  .person-title { font-size: 10.5px; letter-spacing: 1px; color: var(--grey); margin-top: 3px; }

  .divider {
    position: absolute; top: 140px; left: 246px; width: 1px; height: 114px; background: var(--rule);
  }
  .contacts {
    position: absolute; top: 142px; left: 262px; list-style: none;
    font-size: 12.5px; color: var(--black); line-height: 18px;
  }
  .contacts li { display: flex; align-items: center; gap: 8px; white-space: nowrap; }
  .contacts li.continued { padding-left: 18px; }
  .contacts svg { width: 10px; height: 10px; flex: none; }
  .contacts svg .ico { fill: var(--red); }
</style>
</head>
<body>

<section class="card card-back" aria-label="Business card back">
  <div class="brand">
    <span class="brand-mark"></span>
    <span class="brand-name">VOLKAR SYSTEMS</span>
  </div>
</section>

<section class="card card-front" aria-label="Business card front">
  <div class="band band-top-grey"></div>
  <div class="band band-top-red"></div>
  <div class="band band-bottom-red"></div>
  <div class="band band-bottom-grey"></div>

  <div class="brand">
    <span class="brand-mark"></span>
    <span class="brand-name">VOLKAR SYSTEMS</span>
  </div>

  <div class="person">
    <p class="person-name"><span class="first">DEAN</span> HARLOW</p>
    <p class="person-title">SALES MANAGER</p>
  </div>

  <div class="divider"></div>

  <ul class="contacts">
    <li>
      <svg viewBox="0 0 10 10" aria-hidden="true"><rect class="ico" x="2.5" y="0" width="5" height="10" rx="1"/></svg>
      0471 625 183
    </li>
    <li>
      <svg viewBox="0 0 10 10" aria-hidden="true"><path class="ico" d="M2 0h2l1 3-1.5 1a6 6 0 0 0 2.5 2.5L7 5l3 1v2a2 2 0 0 1-2 2A8 8 0 0 1 0 2a2 2 0 0 1 2-2z"/></svg>
      1300 872 619
    </li>
    <li>
      <svg viewBox="0 0 10 10" aria-hidden="true"><path class="ico" d="M0 2h10v6H0z"/><path d="M0 2l5 3.5L10 2" stroke="#fff" stroke-width="0.8" fill="none"/></svg>
      dean@volkarsystems.com.au
    </li>
    <li>
      <svg viewBox="0 0 10 10" aria-hidden="true"><circle class="ico" cx="5" cy="5" r="5"/><path d="M0 5h10M5 0c-3 3-3 7 0 10M5 0c3 3 3 7 0 10" stroke="#fff" stroke-width="0.7" fill="none"/></svg>
      www.volkarsystems.com.au
    </li>
    <li>
      <svg viewBox="0 0 10 10" aria-hidden="true"><path class="ico" d="M5 0a3.5 3.5 0 0 1 3.5 3.5C8.5 6 5 10 5 10S1.5 6 1.5 3.5A3.5 3.5 0 0 1 5 0z"/><circle cx="5" cy="3.5" r="1.2" fill="#fff"/></svg>
      4/18 Galloway Crest Road
    </li>
    <li class="continued">Marlow Heights NSW 2184</li>
  </ul>
</section>

</body>
</html>
```